Airport Advertising Brochure

I need a flyer put together asap! Previous example included. Would like something clean and updated. New logo and updated company name. I would like this designed in Pages or Illustrator so I can update content when needed. Website: pagelantern.com

Target Market(s)

Authors. This page has some good content about what we do: https://www.pagelantern.com/terminaladvertising/

Industry/Entity Type

Airport

Font styles to use
Serif
Sans Serif

Requirements
Must have
• Clean, modern design.

```html
<!DOCTYPE html>
<html lang="en">
<head>
<meta charset="utf-8">
<title>PageLantern – Terminal Advertising</title>
<link rel="stylesheet" href="https://fonts.googleapis.com/css2?family=Raleway:wght@300;400;500;600&display=swap">
<style>
  :root {
    --yellow: #ffdd00;
    --ink: #1f1f1f;
    --text: #3a3a3a;
    --band: #3b3b3c;
    --band-text: #c9c9c9;
    --white: #ffffff;
    --shelf-dark: #1a1c1f;
    --shelf-mid: #4a3b34;
  }
  * { box-sizing: border-box; margin: 0; padding: 0; }
  html, body { width: 848px; height: 1200px; overflow: hidden; background: var(--white); }
  body { font-family: "Raleway", sans-serif; color: var(--text); }
  .flyer { position: relative; width: 848px; height: 1200px; background: var(--white); }

  .accent-block { position: absolute; left: 0; top: 50px; width: 261px; height: 456px; background: var(--yellow); }
  .hero-photo {
    position: absolute; left: 20px; top: 125px; width: 285px; height: 417px;
    background: linear-gradient(160deg, var(--shelf-mid) 0%, var(--shelf-dark) 55%, #2a2f3a 100%);
  }
  .hero-tail { position: absolute; left: 277px; top: 541px; }

  .wordmark {
    position: absolute; left: 329px; top: 62px;
    font-size: 42px; font-weight: 500; color: var(--ink); letter-spacing: -0.5px;
  }

  .values { position: absolute; left: 331px; top: 144px; display: flex; }
  .values p { font-size: 21px; line-height: 25px; color: var(--ink); font-weight: 400; }
  .values p:nth-child(1) { width: 178px; }
  .values p:nth-child(2) { width: 176px; }
  .values p:nth-child(3) { width: 130px; }

  .intro { position: absolute; left: 331px; top: 292px; width: 480px; }
  .intro p { font-size: 15px; line-height: 24.5px; font-weight: 300; color: var(--text); margin-bottom: 17px; }

  .services {
    position: absolute; left: 0; top: 631px; width: 848px; height: 386px;
    background: var(--band); display: flex; padding: 30px 20px 0;
  }
  .service { width: 269px; text-align: center; position: relative; }
  .service + .service::before {
    content: ""; position: absolute; left: 0; top: 53px; height: 278px;
    border-left: 2px dotted var(--yellow);
  }
  .service-icon { display: block; margin: 30px auto 0; width: 64px; height: 64px; }
  .service h2 { font-size: 20px; font-weight: 500; color: var(--white); line-height: 27px; margin-top: 20px; }
  .service p { font-size: 15px; line-height: 23px; font-weight: 300; color: var(--band-text); margin-top: 12px; padding: 0 14px; }
  .service:first-child h2 { margin-top: 20px; }
  .service:first-child p { padding: 0 0 0 0; }

  .footer-brand { position: absolute; left: 28px; top: 1100px; display: flex; align-items: center; gap: 12px; }
  .footer-brand .mark { width: 18px; height: 18px; background: var(--yellow); }
  .footer-brand span { font-size: 22px; font-weight: 500; color: var(--ink); }

  .contact { position: absolute; right: 19px; top: 1062px; text-align: right; font-size: 13px; line-height: 18px; font-weight: 400; color: var(--ink); }
  .contact p { margin-bottom: 17px; }
</style>
</head>
<body>
<main class="flyer">
  <div class="accent-block"></div>
  <div class="hero-photo" role="img" aria-label="Photograph of colourful books on dark library shelves"></div>
  <svg class="hero-tail" width="29" height="30" viewBox="0 0 29 30" aria-hidden="true">
    <polygon points="0,0 28,0 28,29" fill="var(--shelf-dark)"/>
  </svg>

  <h1 class="wordmark">PageLantern</h1>

  <section class="values">
    <p>We are fast &amp; nimble. We are creative and energetic.</p>
    <p>We are dedicated and experienced. Disruption is crucial.</p>
    <p>Flawless execution is paramount.</p>
  </section>

  <section class="intro">
    <p>A book is a powerful weapon, one that establishes direction and provides a plan for growth. It represents the most meaningful narrative of your brand, making way for previously unreachable opportunities. Books are the tip of the thought leadership arrow.</p>
    <p>Writing a book is a challenging endeavor, therefore knowing where and how to direct your energy and resources to create a successful book launch is imperative. That’s why we’re here. We understand the art and science of the publishing world and most important - how to make your book a success.</p>
  </section>

  <section class="services">
    <article class="service">
      <svg class="service-icon" viewBox="0 0 64 64" aria-hidden="true" fill="none" stroke="var(--yellow)" stroke-width="4" stroke-linejoin="round" stroke-linecap="round">
        <path d="M22 42 C26 24 40 12 56 8 C52 24 40 38 22 42 Z"/>
        <circle cx="42" cy="22" r="4"/>
        <path d="M24 30 L12 30 L20 22 L32 20"/>
        <path d="M34 40 L34 52 L42 44 L44 32"/>
        <path d="M18 46 L8 56"/>
      </svg>
      <h2>Book Launch</h2>
      <p>So you wrote a great book. Now what? How do you get it into the hands and minds of the right people, the people who will connect with your idea, rally behind it, and catapult it to new heights?</p>
    </article>
    <article class="service">
      <svg class="service-icon" viewBox="0 0 64 64" aria-hidden="true" fill="none" stroke="var(--yellow)" stroke-width="4" stroke-linejoin="round">
        <rect x="8" y="24" width="10" height="14"/>
        <path d="M18 24 L44 10 L44 52 L18 38 Z"/>
        <path d="M22 40 L26 54 L32 54 L30 42"/>
        <path d="M50 24 L56 22 M50 31 L57 31 M50 38 L56 40" stroke-linecap="round"/>
      </svg>
      <h2>Airport<br>Advertising</h2>
      <p>Airport bookstores are the last remaining bookstores to capture the attention of influencers and decision makers. Imagine the impression made when a potential client</p>
    </article>
    <article class="service">
      <svg class="service-icon" viewBox="0 0 64 64" aria-hidden="true">
        <path d="M6 22 H18 L34 8 V56 L18 42 H6 Z" fill="var(--yellow)"/>
        <path d="M42 22 Q48 32 42 42" fill="none" stroke="var(--yellow)" stroke-width="4" stroke-linecap="round"/>
        <path d="M48 14 Q60 32 48 50" fill="none" stroke="var(--yellow)" stroke-width="4" stroke-linecap="round"/>
      </svg>
      <h2>Speaker<br>Platform</h2>
      <p>Airport bookstores are the last remaining bookstores to capture the attention of influencers and decision makers. Imagine the impression made when a potential client</p>
    </article>
  </section>

  <div class="footer-brand">
    <div class="mark"></div>
    <span>PageLantern</span>
  </div>

  <address class="contact">
    <p>214 Larkspur Ave<br>Portland OR 97205</p>
    <p>+1 (503) 555-0147<br>hello@pagelantern.com</p>
    <p>www.pagelantern.com</p>
  </address>
</main>
</body>
</html>
```